Design a business card & stationary for a mortgage company

We are looking for a good looking business card design for our mortgage company that includes our logo. We received a free design as part of our logo project but we don't love it. The company is called "Pinecrest Mortgage Company" so we like waves and lighthouses. The logo should be included. We have a version in both vertical and horizontal that we have provided.

Industry/Entity Type

Finance

Contact Information for Business Card

This should include our new logo file

Requirements
Must have
• 3. The details you'd like on the card - name, title, phone, email, website, address, social media handles etc.
1. Marcus Hale
Vice President
732-419-6253
Fax 888-304-2918
mhale@pinecrestmortgage.example
NMLS 47162 - Company NMLS 61290
18 Larkin Ave
Millbrook, OR 08614

```html
<!DOCTYPE html>
<html lang="en">
<head>
<meta charset="utf-8">
<title>Pinecrest Mortgage Company – Business Card</title>
<link rel="stylesheet" href="https://fonts.googleapis.com/css2?family=Jost:wght@400;500&family=Arimo:wght@400&display=swap">
<style>
  :root {
    --stage: #151515;
    --card: #2b2b2b;
    --card-edge: #333333;
    --brand-blue: #1d7cc4;
    --accent-blue: #1f95e0;
    --band-blue: #16619f;
    --band-line: #1f8be0;
    --band-text: #0c2442;
    --text-light: #e6e6e6;
  }
  * { margin: 0; padding: 0; box-sizing: border-box; }
  html, body {
    width: 1200px; height: 900px; overflow: hidden;
    background: var(--stage);
  }
  .canvas { position: relative; width: 1200px; height: 900px; }
  .card {
    position: absolute; left: 270px; width: 660px; height: 377px;
    background: var(--card);
    border: 1px solid var(--card-edge);
    box-shadow: 0 10px 30px rgba(0,0,0,.6);
    overflow: hidden;
  }
  .card--logo { top: 40px; }
  .card--contact { top: 480px; }

  .brand-name {
    font-family: "Jost", sans-serif; font-weight: 500;
    color: var(--brand-blue); text-transform: uppercase;
    display: flex; align-items: center; gap: 12px;
    line-height: 1.05;
  }
  .brand-mark {
    width: 14px; height: 14px; border-radius: 50%;
    background: var(--brand-blue); flex: none;
  }
  .card--logo .brand-name {
    position: absolute; left: 0; right: 0; top: 160px;
    justify-content: center; font-size: 44px; letter-spacing: 2px;
  }
  .card--logo .brand-name small {
    display: block; font-size: 17px; letter-spacing: 7px; margin-top: 6px;
  }
  .card--contact .brand-name {
    position: absolute; left: 34px; top: 118px; width: 260px;
    font-size: 33px; letter-spacing: 1px; flex-direction: column; align-items: flex-start; gap: 8px;
  }
  .card--contact .brand-name small { font-size: 13.5px; letter-spacing: 5px; }
  .divider {
    position: absolute; left: 318px; top: 82px; width: 2px; height: 178px;
    background: var(--accent-blue);
  }
  .person { position: absolute; left: 348px; top: 82px; }
  .person__name {
    font-family: "Jost", sans-serif; font-weight: 500; font-size: 31px;
    color: var(--accent-blue); text-transform: uppercase; letter-spacing: 2px;
  }
  .person__title {
    font-family: "Arimo", sans-serif; font-size: 17px; color: var(--text-light);
    margin-top: -2px;
  }
  .contacts { list-style: none; margin-top: 22px; }
  .contacts li {
    font-family: "Arimo", sans-serif; font-size: 16px; color: var(--text-light);
    display: flex; align-items: center; gap: 9px; height: 25px;
  }
  .contacts svg { width: 13px; height: 13px; flex: none; }
  .band {
    position: absolute; left: 0; right: 0; bottom: 0; height: 52px;
    background: var(--band-blue); border-top: 3px solid var(--band-line);
    font-family: "Arimo", sans-serif; font-size: 18px; color: var(--band-text);
    display: flex; align-items: center; justify-content: center; white-space: nowrap;
  }
</style>
</head>
<body>
<main class="canvas">
  <section class="card card--logo" aria-label="Card reverse">
    <div class="brand-name">
      <span class="brand-mark"></span>
      <span>Pinecrest<small>Mortgage Company</small></span>
    </div>
  </section>

  <section class="card card--contact" aria-label="Card front">
    <div class="brand-name">
      <span class="brand-mark"></span>
      <span>Pinecrest</span>
      <small>Mortgage Company</small>
    </div>
    <div class="divider"></div>
    <div class="person">
      <h1 class="person__name">Marcus Hale</h1>
      <p class="person__title">Vice President</p>
      <ul class="contacts">
        <li>
          <svg viewBox="0 0 16 16" aria-hidden="true"><path fill="#1f95e0" d="M4 1l3 3-2 2c1 2 3 4 5 5l2-2 3 3-2 3C7 15 1 9 1 3z"/></svg>
          541-419-6253
        </li>
        <li>
          <svg viewBox="0 0 16 16" aria-hidden="true"><rect x="4" y="1" width="8" height="5" fill="#1f95e0"/><rect x="1" y="6" width="14" height="6" rx="1" fill="#1f95e0"/><rect x="4" y="10" width="8" height="5" fill="#1f95e0"/></svg>
          888-304-2918
        </li>
        <li>
          <svg viewBox="0 0 16 16" aria-hidden="true"><rect x="1" y="3" width="14" height="10" fill="none" stroke="#1f95e0" stroke-width="1.5"/><path d="M1 3l7 6 7-6" fill="none" stroke="#1f95e0" stroke-width="1.5"/></svg>
          mhale@pinecrestmortgage.example
        </li>
        <li>
          <svg viewBox="0 0 16 16" aria-hidden="true"><g fill="none" stroke="#1f95e0" stroke-width="1.2"><circle cx="8" cy="8" r="6.5"/><ellipse cx="8" cy="8" rx="3" ry="6.5"/><path d="M1.5 8h13M2.5 5h11M2.5 11h11"/></g></svg>
          www.pinecrestmortgage.example
        </li>
      </ul>
    </div>
    <div class="band">NMLS 47162 - Company NMLS 61290 18 Larkin Ave Millbrook, OR 08614</div>
  </section>
</main>
</body>
</html>
```